Letterhead to coordinate with business card

I am needing a docx template and print file for a letterhead to co-ordinate with my newly designed logo and business card.

```html
<!DOCTYPE html>
<html lang="en">
<head>
<meta charset="utf-8">
<title>Harbourline Plan Services – Letterhead</title>
<link href="https://fonts.googleapis.com/css2?family=Arimo:wght@400;700&family=Source+Sans+3:wght@400&display=swap" rel="stylesheet">
<style>
  :root {
    --plum: #982c60;
    --teal: #127b79;
    --ink: #3a3a3c;
    --ink-soft: #4a4a4d;
    --paper: #f7f7f8;
    --backdrop: #d9dadc;
  }
  * { box-sizing: border-box; margin: 0; padding: 0; }
  html, body { width: 1200px; height: 1141px; overflow: hidden; }
  body {
    background: var(--backdrop);
    font-family: "Arimo", Arial, sans-serif;
    color: var(--ink);
    position: relative;
  }
  .letterhead {
    position: absolute;
    left: 208px;
    top: 20px;
    width: 784px;
    height: 1101px;
    background: var(--paper);
  }
  .brand {
    position: absolute;
    top: 54px;
    left: 0;
    width: 100%;
    display: flex;
    flex-direction: column;
    align-items: center;
    gap: 14px;
  }
  .brand-square {
    width: 76px;
    height: 76px;
    background: var(--plum);
  }
  .brand-name {
    font-family: "Arimo", Arial, sans-serif;
    font-weight: 700;
    font-size: 24px;
    letter-spacing: 1px;
    color: var(--plum);
  }
  .salutation {
    position: absolute;
    left: 59px;
    top: 355px;
    font-size: 18px;
    color: var(--ink);
  }
  .letter-body {
    position: absolute;
    left: 59px;
    top: 414px;
    width: 668px;
    font-size: 11px;
    line-height: 16.7px;
    color: var(--ink-soft);
    text-align: justify;
  }
  .letter-body p { margin-bottom: 16.6px; }
  .closing {
    position: absolute;
    left: 58px;
    top: 783px;
    font-size: 11px;
    color: var(--ink-soft);
  }
  .signature {
    position: absolute;
    left: 58px;
    top: 810px;
    width: 84px;
    height: 36px;
    background: linear-gradient(90deg, #e7e7ea, #dcdde1);
  }
  .contact-line {
    position: absolute;
    left: 0;
    top: 1055px;
    width: 100%;
    text-align: center;
    font-family: "Source Sans 3", "Myriad Pro", sans-serif;
    font-size: 11.5px;
    color: #2a2a2c;
  }
  .rule {
    position: absolute;
    left: 0;
    width: 100%;
    height: 4px;
  }
  .rule-plum { top: 1085px; background: var(--plum); }
  .rule-teal { top: 1094px; background: var(--teal); }
</style>
</head>
<body>
  <main class="letterhead">
    <header class="brand">
      <div class="brand-square"></div>
      <div class="brand-name">Harbourline Plan Services</div>
    </header>

    <p class="salutation">Dear Mr. Carter,</p>

    <section class="letter-body">
      <p>Lorem ipsum dolor sit amet, consectetur adipiscing elit. Donec orci purus, luctus vitae dignissim eu, iaculis sed purus. Vivamus faucibus, ipsum nec aliquet viverra, leo mauris condimentum ligula, sit amet sagittis enim ligula quis arcu. Nam egestas tortor id nisi porttitor mattis. In tortor ante, ultricies in suscipit a, tempus non massa. Vivamus et auctor mi. Fusce vel massa nulla. Phasellus nec eros mauris, et scelerisque orci.</p>
      <p>Donec malesuada orci vitae nulla accumsan porta a id massa. Quisque accumsan iaculis magna sit amet fringilla. Maecenas consequat, magna eget tincidunt semper, odio nibh rutrum mi, id feugiat ante nisi eu risus. Vestibulum nunc orci, rhoncus a placerat in, ultricies in mi. Cras mattis varius eros, vel fringilla nisi suscipit eget. Quisque scelerisque sagittis nulla at porttitor.</p>
      <p>Sed id augue vitae urna euismod commodo aliquet a quam. Pellentesque arcu velit, cursus et malesuada ut, consequat et diam. Nullam erat sem, rhoncus id ullamcorper vitae, rhoncus et arcu. In ultricies ultricies nulla, ut rutrum nisi iaculis at. Donec eu magna a metus ornare faucibus. Fusce aliquet faucibus ultricies. Morbi semper, est id tincidunt gravida, sem arcu adipiscing lacus, ac bibendum nulla leo eu purus. Quisque nec diam sed risus consectetur a ccumsan quis quis nibh. Vestibulum id purus lorem.</p>
      <p>It is a long established fact that a reader will be distracted by the readable content of a page when looking at its layout. The point of using Lorem Ipsum is that it has a more-or-less normal distribution of letters, as opposed to using 'Content here, content here', making it look like readable English. Many desktop publishing packages</p>
      <p>ada ut, consequat et diam. Nullam erat sem, rhoncus id ullamcorper vitae, rhoncus et arcu. In ultricies ultricies nulla, ut rutrum nisi iaculis at. Donec eu magna a metus ornare faucibus. Fusce aliquet faucibus ultricies. Morbi semper,</p>
    </section>

    <p class="closing">Sincerely,</p>
    <div class="signature" role="img" aria-label="Handwritten signature of the sender"></div>

    <footer>
      <p class="contact-line">PO Box 204, Lakeview NSW 2400 | 0400 123 987 | hello@harbourlineplans.com.au | www.harbourlineplans.com.au</p>
      <div class="rule rule-plum"></div>
      <div class="rule rule-teal"></div>
    </footer>
  </main>
</body>
</html>
```